Harbor Light Church San Francisco needs a Leadership Booklet designed.

We need a Leadership Booklet to be designed and formatted. The content is currently 27 pages and involves headings, quotes, bolded statements and scripture that we would like to stick out. We also need a cover designed for it as well. Cover - "Harbor Light Leadership Development"

Here is a link to our Harbor Light Church style guide.
https://studio-51832.brandvault-example.com/d/7QwRnBzK2Lp9/harbor-light-church-style-guide

Target Market(s)

Leaders within our church.

Font styles to use
Sans Serif

```html
<!DOCTYPE html>
<html lang="en">
<head>
<meta charset="utf-8">
<title>Harbor Light Leadership Development – Spread</title>
<link href="https://fonts.googleapis.com/css2?family=Arimo:ital,wght@0,400;0,700;1,400;1,700&family=Jost:wght@400;700&display=swap" rel="stylesheet">
<style>
  :root {
    --backdrop: #e4e4e4;
    --paper: #ffffff;
    --ink: #1d1d1d;
    --rule: #d9d9d9;
    --stripe: #e2e2e2;
    --folio: #d6d6d6;
    --folio-ink: #555555;
  }
  * { box-sizing: border-box; margin: 0; padding: 0; }
  html, body { width: 1200px; height: 939px; overflow: hidden; }
  body {
    background: var(--backdrop);
    font-family: "Arimo", Arial, sans-serif;
    color: var(--ink);
    display: flex;
    align-items: center;
    justify-content: center;
  }
  .spread { display: flex; width: 1120px; height: 820px; background: var(--paper); box-shadow: 0 8px 30px rgba(0,0,0,.15); }
  .page { position: relative; width: 560px; height: 820px; padding: 190px 58px 0 58px; }
  .page--left { border-right: 1px solid #eeeeee; }
  .page-header { position: absolute; top: 42px; left: 58px; right: 58px; display: flex; align-items: center; gap: 14px; }
  .page--right .page-header { flex-direction: row-reverse; }
  .brand { display: flex; align-items: center; gap: 6px; font-family: "Jost", sans-serif; font-weight: 400; font-size: 13px; color: var(--ink); white-space: nowrap; }
  .brand-mark { width: 9px; height: 9px; background: var(--ink); }
  .stripes { flex: 1; display: flex; flex-direction: column; gap: 4px; }
  .stripes span { display: block; height: 4px; background: var(--stripe); }
  .page-footer { position: absolute; bottom: 52px; left: 10px; right: 10px; height: 1px; background: var(--rule); }
  .folio { position: absolute; top: -9px; width: 18px; height: 18px; border-radius: 50%; background: var(--folio); color: var(--folio-ink); font-size: 8px; line-height: 18px; text-align: center; }
  .page--left .folio { right: 60px; }
  .page--right .folio { left: 50px; }
  p { font-size: 10px; line-height: 13.2px; margin-bottom: 11px; }
  .scripture, .statement { font-weight: 700; }
  .quote { font-style: italic; margin-bottom: 11px; }
  .quote p { margin-bottom: 0; }
  .quote cite { display: block; font-weight: 700; font-size: 10px; line-height: 13.2px; }
  .section-title { font-family: "Jost", sans-serif; font-weight: 700; font-size: 21px; letter-spacing: .3px; margin-bottom: 12px; text-transform: uppercase; }
  .page--right { padding-top: 172px; }
</style>
</head>
<body>
<main class="spread">
  <section class="page page--left">
    <header class="page-header">
      <div class="brand"><span class="brand-mark"></span>Harbor Light Church</div>
      <div class="stripes"><span></span><span></span><span></span></div>
    </header>

    <p class="scripture">3 Now Moses was tending the flock of Jethro his father-in-law, the priest of Midian, and he led the flock to the far side of the wilderness and came to Horeb, the mountain of God. 2 There the angel of the Lord appeared to him in flames of fire from within a bush. Moses saw that though the bush was on fire it did not burn up. 3 So Moses thought, “I will go over and see this strange sight—why the bush does not burn up.”</p>
    <p class="scripture">4 When the Lord saw that he had gone over to look, God called to him from within the bush, “Moses! Moses!”</p>
    <p class="scripture">And Moses said, “Here I am.”</p>
    <p class="scripture">5 “Do not come any closer,” God said. “Take off your sandals, for the place where you are standing is holy ground.” 6 Then he said, “I am the God of your father,[a] the God of Abraham, the God of Isaac and the God of Jacob.” At this, Moses hid his face, because he was afraid to look at God.</p>
    <p class="scripture">7 The Lord said, “I have indeed seen the misery of my people in Egypt. I have heard them crying out because of their slave drivers, and I am concerned about their suffering. 8 So I have come down to rescue them from the hand of the Egyptians and to bring them up out of that land into a good and spacious land, a land flowing with milk and honey—the home of the Canaanites, Hittites, Amorites, Perizzites, Hivites and Jebusites. 9 And now the cry of the Israelites has reached me, and I have seen the way the Egyptians are oppressing them. 10 So now, go. I am sending you to Pharaoh to bring my people the Israelites out of Egypt.”</p>
    <p>Notice how this begins. We are simply told about all that God is doing. God heard. God remembered. God looked. God was concerned. So far, the only one playing a part is God.</p>
    <p>Then comes the infamous burning bush experience. Moses was tending the flock of Jethro, his father-in-law. God gets his attention. Then God lets him know what He has seen and how He is concerned. God says, “I have come down to rescue them.” This had to make Moses excited, but he must have wondered, “Why is God telling all of this to me?”</p>
    <p>In verse 10, we learn why God is telling this to Moses. “So now, go. I am sending you to bring my people the Israelites out of Egypt.”</p>
    <p class="statement">Perhaps, part of the reason God has sent you to San Francisco at this time is because he wants you to play a part in helping us accomplish the vision He has given Harbor Light Church.</p>
    <p>Can you see what God is doing in Harbor Light and in San Francisco? How might He be calling you to be a part of it?</p>

    <footer class="page-footer"><span class="folio">2</span></footer>
  </section>

  <section class="page page--right">
    <header class="page-header">
      <div class="brand"><span class="brand-mark"></span>Harbor Light Church</div>
      <div class="stripes"><span></span><span></span><span></span></div>
    </header>

    <h1 class="section-title">Who Harbor Light Leaders Are</h1>
    <p>As Christian leaders, never forget this:<br><strong>WE ARE FOLLOWERS BEFORE WE ARE LEADERS.</strong></p>
    <p>Before we lead others, let’s make sure we are orienting our entire lives around Jesus. We can’t give others what we lack ourselves. Never forget what Jesus said in John 15:5, “I am the vine; you are the branches. If you remain in me and I in you, you will bear much fruit; apart from me you can do nothing.”</p>
    <p>One of the greatest leadership lessons we can learn from watching other leaders throughout the world is this:</p>
    <p class="statement">It is dangerous to have an outer life that your inner life cannot keep up with.</p>
    <blockquote class="quote">
      <p>“One of the great and subtle temptations of leadership is to neglect the inner life and your relationship with God because of the many things which demand immediate attention.”</p>
      <cite>- Martin Hale, The Quiet Work of Leading</cite>
    </blockquote>
    <blockquote class="quote">
      <p>“Because my inner life is invisible, it is easy to neglect.”</p>
      <cite>- Jonah Pell, Inner Ground</cite>
    </blockquote>
    <blockquote class="quote">
      <p>“The most important thing in your life is not what you do; it’s who you become.”</p>
      <cite>- Darren Whitlow</cite>
    </blockquote>
    <p class="scripture">Philippians 1:6 being confident of this, that he who began a good work in you will carry it on to completion until the day of Christ Jesus.</p>
    <p class="scripture">Galatians 4:19 My dear children, for whom I am again in the pains of childbirth until Christ is FORMED in you</p>
    <p>Christian leadership certainly has a lot to do with the work that we do for God and we’ll get there in the next section. We’re mostly interested in what we can produce in this world, but God is mostly interested in what He can produce in us. Here’s a question we should ask:</p>
    <p class="statement">How can I position myself so that God can do His work in me?</p>
    <p class="scripture">Luke 6:43-45 “No good tree bears bad fruit, nor does a bad tree bear good fruit. 44 Each tree is recognized by its own fruit. People do not pick figs from thornbushes, or grapes from briers. 45 A good man brings good things out of the good stored up in his heart, and</p>

    <footer class="page-footer"><span class="folio">3</span></footer>
  </section>
</main>
</body>
</html>
```